galactic arcade 80s vibes - jewelry company

I am looking for someone to build me a website for my jewelry company - I am going for an 80s retro GALACTIC arcade vibe. I want it to feel old school, be brightly colored (purples, greens, etc) encompass planets, stars, or milky way type vibes. My company is called LumoKitt - it is zodiac signs & angel number jewelry. I want the website to open up as galaxy and my logo/name to pop up in the center of the screen and then go to the main page.

Industry/Entity Type

jewelry

Coding

Coded - Design and coding required

Number of Pages Required

1 page

Font styles to use
Other font styles liked:
• retro

Colors
0094D4
00A9DD
6FCCEA
C7EBF8
E9F6FB
00AB8E
00BBA5
67D7C9
C6EFE9
E9F9F6
59FF00
82FF00
B8FF75
E3FFCB
F4FFEA
FFF300
FFF600
FEFA6F
FFFEC7
FFFEE8
FFC000
F8CF3A
FAE287
FDF2CF
FEFAEE
E54698
E96AAD
F1A4CE
F9D9EA
FCEFF6
A7469A
B969AE
D3A5CF
EDDBEB
F8F0F9
6B429C
8869AF
B7A5CE
E3DAEB
F3F0F8

```html
<!DOCTYPE html>
<html lang="en">
<head>
<meta charset="utf-8">
<title>LumoKitt — Galactic Jewelry</title>
<link rel="stylesheet" href="https://fonts.googleapis.com/css2?family=Exo+2:ital,wght@0,800;0,900;1,800;1,900&family=Poppins:wght@400;500;600&family=Teko:wght@500;600&display=swap">
<style>
:root{
  --page:#ffffff;
  --night:#05002e;
  --night-2:#0b0440;
  --plum:#26033f;
  --plum-2:#32074f;
  --plum-3:#3c0a5e;
  --card:#2d0648;
  --violet:#9b1ff2;
  --violet-bright:#b13cff;
  --lilac:#a774ff;
  --pink:#e54698;
  --white:#ffffff;
  --muted:#e8dcf5;
}
*{margin:0;padding:0;box-sizing:border-box}
html,body{width:1200px;height:3972px;overflow:hidden}
body{background:var(--page);font-family:"Poppins",sans-serif;color:var(--white);position:relative}
.screen{position:absolute;left:29px;width:1138px;overflow:hidden}
.screen--intro{top:31px;height:610px;background:var(--night)}
.screen--main{top:663px;height:3256px;background:var(--plum)}

.nav{position:absolute;left:0;right:0;top:44px;height:50px;display:flex;align-items:center;padding:0 104px 0 108px;z-index:3}
.brand{font-family:"Exo 2",sans-serif;font-weight:900;font-size:32px;letter-spacing:1px;color:var(--white)}
.nav__links{display:flex;gap:40px;margin-left:auto;margin-right:42px;font-size:14.5px}
.nav__links a{color:var(--white);text-decoration:none}
.nav__links a.is-active{color:var(--lilac)}
.btn{display:inline-flex;align-items:center;justify-content:center;border:2px solid var(--violet-bright);border-radius:6px;background:var(--night);color:var(--white);font-family:"Exo 2",sans-serif;font-weight:900;font-size:14px;letter-spacing:.5px;box-shadow:0 0 8px rgba(177,60,255,.6);text-transform:uppercase}
.nav .btn{width:123px;height:48px}

.scene{position:absolute;left:0;right:0;bottom:0;background:linear-gradient(180deg,var(--night) 0%,var(--night) 38%,#3a0a5c 55%,#c2407d 62%,#4b0f7a 72%,#1d0642 100%)}
.screen--intro .scene{top:0}
.intro__title{position:absolute;top:265px;left:0;right:0;text-align:center;font-family:"Exo 2",sans-serif;font-weight:900;font-size:70px;letter-spacing:1px}

.hero{position:relative;height:606px;background:var(--night)}
.hero .scene{top:90px;bottom:0}
.hero__copy{position:absolute;top:220px;left:0;right:0;text-align:center;z-index:2}
.hero__title{font-family:"Exo 2",sans-serif;font-style:italic;font-weight:900;font-size:41px;letter-spacing:.5px}
.hero__text{font-size:15px;line-height:23px;margin:14px auto 0;width:470px}
.hero .btn{width:136px;height:46px;margin-top:20px}
.wave{position:absolute;left:0;width:1138px;display:block;z-index:2}

.section-title{font-family:"Exo 2",sans-serif;font-style:italic;font-weight:900;font-size:42px;text-align:center;letter-spacing:.5px}
.section-title .accent{color:var(--violet)}
.section-title--glow{color:var(--violet);text-shadow:0 0 10px rgba(177,60,255,.7)}

.about{position:relative;height:561px;background:linear-gradient(180deg,var(--plum) 0%,#220238 100%)}
.about__photo{position:absolute;left:103px;top:57px;width:446px;height:424px;border:3px solid var(--violet);border-radius:16px;background:radial-gradient(circle at 45% 45%,#bdbdbd 0%,#5c5c5c 22%,#111 48%,#000 70%);box-shadow:0 0 12px rgba(155,31,242,.55)}
.about__body{position:absolute;left:593px;top:112px;width:445px}
.about__body .section-title{text-align:left;font-size:41px}
.about__body p{font-size:14.3px;line-height:23px;text-align:justify;margin-top:14px;color:var(--muted)}
.about__body p + p{margin-top:6px}
.about .btn{width:133px;height:48px;margin-top:20px}

.services{position:relative;height:692px;background:radial-gradient(circle at 50% 30%,#4a0f70 0%,var(--plum-3) 30%,var(--plum-2) 70%)}
.services .section-title{padding-top:80px}
.cards{display:flex;gap:21px;width:924px;margin:40px auto 0}
.card{width:294px;height:354px;background:var(--card);border-radius:6px;text-align:center;padding-top:26px}
.card svg{width:120px;height:106px}
.card__title{font-family:"Exo 2",sans-serif;font-style:italic;font-weight:900;font-size:25px;color:var(--violet);margin-top:8px}
.card__text{font-size:14px;line-height:26px;width:240px;margin:6px auto 0}
.card__link{display:inline-block;font-family:"Exo 2",sans-serif;font-weight:800;font-size:14.5px;color:var(--violet);margin-top:8px;padding-bottom:4px;border-bottom:3px solid var(--violet);text-decoration:none}

.products{position:relative;height:562px;background:linear-gradient(180deg,#1f0236 0%,var(--plum) 100%)}
.products .section-title{padding-top:68px}
.product-row{display:flex;gap:20px;width:924px;margin:62px auto 0}
.product{position:relative;width:216px;height:294px}
.product__photo{position:absolute;inset:0}
.product__photo--pearl{background:linear-gradient(135deg,#d8d4cf,#a39c93 55%,#e6e2dd)}
.product__photo--halo{background:radial-gradient(circle at 55% 50%,#bdbdbd 0%,#555 25%,#1c1c1c 60%)}
.product__photo--oval{background:radial-gradient(circle at 50% 50%,#d9d6cf 0%,#8b8678 35%,#403b33 80%)}
.product__photo--emerald{background:radial-gradient(circle at 60% 40%,#8a5f8a 0%,#5a5a5a 30%,#2b2b2b 75%)}
.product.is-hover{outline:3px solid var(--violet);}
.tag{position:absolute;left:10px;top:14px;background:var(--violet);color:var(--white);font-size:12px;font-weight:600;padding:1px 9px;border-radius:3px}
.product.is-hover .tag{top:6px}
.product__actions{position:absolute;right:10px;top:10px;display:flex;flex-direction:column;gap:10px}
.product__actions span{width:26px;height:26px;border-radius:50%;background:var(--violet);display:flex;align-items:center;justify-content:center}
.product__name{position:absolute;left:0;right:0;bottom:30px;text-align:center;font-family:"Teko",sans-serif;font-weight:500;font-size:24px}

.reviews{position:relative;height:492px;background:linear-gradient(180deg,#3a0b5a 0%,var(--plum-2) 60%,var(--plum-2) 100%)}
.reviews .section-title{padding-top:90px}
.quote{position:relative;width:860px;margin:30px auto 0;text-align:center;font-size:14px;line-height:25px;color:var(--muted)}
.quote__mark{position:absolute;font-family:"Exo 2",sans-serif;font-weight:900;font-size:40px;color:#8a6aa3;line-height:1}
.quote__mark--open{left:-14px;top:-6px}
.quote__mark--close{right:140px;bottom:-26px}
.reviewer{font-family:"Teko",sans-serif;font-weight:500;font-size:22px;color:var(--violet);text-align:center;margin-top:20px}
.reviews .btn{display:flex;width:166px;height:50px;margin:10px auto 0;font-family:"Teko",sans-serif;font-weight:500;font-size:18px;text-transform:none;letter-spacing:0}

.footer{position:relative;height:343px;background:var(--plum);text-align:center}
.footer .brand{display:block;font-size:60px;padding-top:60px;line-height:72px}
.footer__links{display:flex;justify-content:center;gap:18px;font-size:14.5px;margin-top:22px}
.footer__links span.sep{opacity:.9}
.social{display:flex;justify-content:center;gap:12px;margin-top:24px}
.social span{width:30px;height:30px;border:2px solid var(--violet);border-radius:50%}
.copyright{font-size:13.5px;margin-top:28px}
</style>
</head>
<body>

<section class="screen screen--intro">
  <div class="scene" role="img" aria-label="Retro synthwave landscape: neon purple mountains, glowing sunset and a pink grid road leading to a distant city"></div>
  <nav class="nav">
    <span class="brand">LUMOKITT</span>
    <div class="nav__links"><a href="#">Home</a><a href="#">About</a><a href="#">What Wedo</a><a href="#">Product</a><a href="#">Reviuew</a></div>
    <a class="btn" href="#">Contact Us</a>
  </nav>
  <h1 class="intro__title">LUMOKITT</h1>
</section>

<main class="screen screen--main">
  <header class="hero">
    <div class="scene" role="img" aria-label="Retro synthwave landscape: neon purple mountains, glowing sunset and a pink grid road leading to a distant city"></div>
    <nav class="nav">
      <span class="brand">LUMOKITT</span>
      <div class="nav__links"><a class="is-active" href="#">Home</a><a href="#">About</a><a href="#">What Wedo</a><a href="#">Product</a><a href="#">Reviuew</a></div>
      <a class="btn" href="#">Contact Us</a>
    </nav>
    <div class="hero__copy">
      <h2 class="hero__title">WELCOME TO LUMOKITT</h2>
      <p class="hero__text">Lorem ipsum dolor sit amet, consectetur adipiscing elit, sed do eiusmod tempor incididunt dolore magna aliqua.</p>
      <a class="btn" href="#">Get Started</a>
    </div>
    <svg class="wave" style="bottom:0" height="72" viewBox="0 0 1138 72" preserveAspectRatio="none">
      <path d="M0 72 L0 62 C180 8 420 -4 640 30 C860 62 1010 52 1138 30 L1138 72 Z" fill="#26033f"/>
      <path d="M0 62 C180 8 420 -4 640 30 C860 62 1010 52 1138 30" fill="none" stroke="#a020f0" stroke-width="7"/>
    </svg>
  </header>

  <section class="about">
    <div class="about__photo" role="img" aria-label="Silver ring with three round diamonds on a black background"></div>
    <div class="about__body">
      <h2 class="section-title">ABOUT TO <span class="accent">LUMOKITT</span></h2>
      <p>Lorem ipsum dolor sit amet, consectetur adipiscing elit, sed do eiusmod tempor incididunt ut labore et dolore magna aliqua. Ut enim ad minim veniam, quis nostrud exercitation ullamco laboris nisi ut aliquip ex ea commodo consequat.</p>
      <p>Sed ut perspiciatis unde omnis iste natus error sit voluptatem accusantium doloremque laudantium, totam rem aperiam, eaque ipsa quae ab illo inventore veritatis et quasi architecto beatae vitae dicta sunt explicabo.</p>
      <a class="btn" href="#">Read More</a>
    </div>
  </section>

  <section class="services">
    <h2 class="section-title">WHAT <span class="accent">WE DO</span></h2>
    <div class="cards">
      <article class="card">
        <svg viewBox="0 0 120 106" fill="none" stroke="#9b1ff2" stroke-width="5" stroke-linejoin="round">
          <rect x="12" y="8" width="22" height="86" rx="8"/>
          <path d="M34 20 H110 V94 H34"/>
          <path d="M52 82 L92 42 L100 50 L60 90 Z"/>
          <path d="M52 82 V40 L84 72"/>
        </svg>
        <h3 class="card__title">Design</h3>
        <p class="card__text">Lorem ipsum dolor sit amet, consectetur adipiscing elit, sed do eiusmod tempor incididunt aliqua.</p>
        <a class="card__link" href="#">Read More</a>
      </article>
      <article class="card">
        <svg viewBox="0 0 120 106" fill="none" stroke="#9b1ff2" stroke-width="5" stroke-linejoin="round" stroke-linecap="round">
          <rect x="14" y="16" width="92" height="62" rx="6"/>
          <path d="M4 92 H116"/>
          <path d="M46 36 L34 47 L46 58 M74 36 L86 47 L74 58 M64 32 L56 62"/>
        </svg>
        <h3 class="card__title">Development</h3>
        <p class="card__text">Lorem ipsum dolor sit amet, consectetur adipiscing elit, sed do eiusmod tempor incididunt aliqua.</p>
        <a class="card__link" href="#">Read More</a>
      </article>
      <article class="card">
        <svg viewBox="0 0 120 106" fill="none" stroke="#9b1ff2" stroke-width="5" stroke-linejoin="round" stroke-linecap="round">
          <path d="M24 58 L70 22 L90 70 L36 76 Z"/>
          <path d="M24 58 L14 62 L20 80 L36 76"/>
          <path d="M40 76 L48 96 L58 92 L52 75"/>
          <path d="M82 20 L88 8 M96 34 L110 30 M92 26 L104 16"/>
        </svg>
        <h3 class="card__title">Marketing</h3>
        <p class="card__text">Lorem ipsum dolor sit amet, consectetur adipiscing elit, sed do eiusmod tempor incididunt aliqua.</p>
        <a class="card__link" href="#">Read More</a>
      </article>
    </div>
  </section>

  <section class="products">
    <h2 class="section-title section-title--glow">PRODUCT</h2>
    <div class="product-row">
      <article class="product">
        <div class="product__photo product__photo--pearl" role="img" aria-label="Twisted gold and silver ring with a pearl"></div>
        <span class="tag">New</span>
      </article>
      <article class="product">
        <div class="product__photo product__photo--halo" role="img" aria-label="Halo diamond ring on dark fabric"></div>
        <span class="tag">New</span>
      </article>
      <article class="product is-hover">
        <div class="product__photo product__photo--oval" role="img" aria-label="Oval diamond ring on a grey surface"></div>
        <span class="tag">New</span>
        <div class="product__actions">
          <span><svg width="12" height="12" viewBox="0 0 12 12" fill="#fff"><path d="M0 1h2l1.5 6h6L11 3H3.2" stroke="#fff" stroke-width="1.4" fill="none"/><circle cx="4.5" cy="10" r="1.2"/><circle cx="8.5" cy="10" r="1.2"/></svg></span>
          <span><svg width="12" height="12" viewBox="0 0 12 12"><path d="M6 11 L1.2 6.2 A2.8 2.8 0 0 1 6 2.4 A2.8 2.8 0 0 1 10.8 6.2 Z" fill="#fff"/></svg></span>
        </div>
        <p class="product__name">Lorem ipsum</p>
      </article>
      <article class="product">
        <div class="product__photo product__photo--emerald" role="img" aria-label="Silver ring with a purple emerald-cut stone and diamond halo"></div>
        <span class="tag">New</span>
      </article>
    </div>
  </section>

  <section class="reviews">
    <h2 class="section-title section-title--glow">REVIEWS</h2>
    <blockquote class="quote">
      <span class="quote__mark quote__mark--open">“</span>
      Lorem ipsum dolor sit amet, consectetur adipiscing elit, sed do eiusmod tempor incididunt ut labore et dolore magna aliqua. Ut enim ad minim veniam, quis nostrud exercitation ullamco laboris nisi ut aliquip ex ea commodo consequat. Lorem ipsum dolor sit amet, consectetur adipiscing elit, sed do eiusmod tempor incididunt ut labore et dolore magna aliqua. Ut enim ad minim veniam, quis nostrud exercitation ullamco laboris nisi ut aliquip ex ea commodo consequat.
      <span class="quote__mark quote__mark--close">”</span>
    </blockquote>
    <p class="reviewer">Lorem ipsum</p>
    <a class="btn" href="#">View More Testimonials</a>
    <svg class="wave" style="bottom:0" height="70" viewBox="0 0 1138 70" preserveAspectRatio="none">
      <path d="M0 70 L0 24 C200 -6 420 10 640 40 C860 68 1020 50 1138 6 L1138 70 Z" fill="#26033f"/>
      <path d="M410 14 C480 22 560 30 640 40 C860 68 1020 50 1138 6" fill="none" stroke="#a020f0" stroke-width="7"/>
    </svg>
  </section>

  <footer class="footer">
    <span class="brand">LUMOKITT</span>
    <nav class="footer__links">
      <span>Home</span><span class="sep">|</span><span>About</span><span class="sep">|</span><span>What Wedo</span><span class="sep">|</span><span>Product</span><span class="sep">|</span><span>Reviuew</span><span class="sep">|</span><span>Contact Us</span>
    </nav>
    <div class="social"><span></span><span></span><span></span><span></span></div>
    <p class="copyright">©Copyrights 2022 LumoKitt | All Rights Reserved</p>
  </footer>
</main>

</body>
</html>
```